Anatomic 3D models + Urological Robotic surgery site

I want a website to represent my business as a developer of 3D models (reconstructions based on CT and MRI scans) and urological robotic surgery. The main point I need on my website is that it is modern, very attractive, clean, responsive and an interaction that differentiate me from the usual websites they have in my market. The site will be in portuguese and I'll provide the content to be used. The company name would be my name: Dr Renato Vilhena. The colors and other choices I made here are not final decisions. If you have a suggestion you, they are welcome.

Target Market(s)

My patients

Industry/Entity Type

Medical

Coding

Number of Pages Required

1 page

Font styles to use
Sans Serif

Colors
0054AA
0677BA
7BADD7
CADEEF
E8F1F8
0094D4
00A9DD
6FCCEA
C7EBF8
E9F6FB
00AB8E
00BBA5
67D7C9
C6EFE9
E9F9F6
59FF00
82FF00
B8FF75
E3FFCB
F4FFEA
FFC000
F8CF3A
FAE287
FDF2CF
FEFAEE
F0912C
F2A743
F7CA91
FBE8D2
FDF5EE
A7469A
B969AE
D3A5CF
EDDBEB
F8F0F9
6B429C
8869AF
B7A5CE
E3DAEB
F3F0F8

Requirements
Must have
• Responsive, clean, modern, attractive, stand out from usual sites.
Should not have
• Antiquate boring designs.

```html
<!DOCTYPE html>
<html lang="en">
<head>
<meta charset="utf-8">
<title>Dr Renato Vilhena — Urology &amp; Robotic Surgery</title>
<link rel="stylesheet" href="https://fonts.googleapis.com/css2?family=Syncopate:wght@400;700&family=Montserrat:wght@400;500;600;700&display=swap">
<style>
:root{
  --purple:#6B429C;
  --purple-soft:#8869AF;
  --blue:#0054AA;
  --blue-mid:#0677BA;
  --cyan:#00A9DD;
  --teal:#00AB8E;
  --teal-light:#00BBA5;
  --navy:#1E1B4B;
  --ink:#1d1d3a;
  --text:#3a3a55;
  --pale:#EEF0F8;
  --white:#ffffff;
}
*{margin:0;padding:0;box-sizing:border-box}
html,body{width:1200px;height:5324px;overflow:hidden}
body{font-family:"Montserrat",sans-serif;color:var(--text);background:var(--white);position:relative}
.abs{position:absolute}
.display{font-family:"Syncopate",sans-serif;text-transform:uppercase;color:var(--ink);letter-spacing:2px}
.display .light{font-weight:400;display:block}
.display .bold{font-weight:700;display:block}
.center{text-align:center;left:0;width:1200px}
.rule{width:56px;height:3px;background:linear-gradient(90deg,var(--blue),var(--purple));margin:10px auto 0}

/* hero */
.hero{left:0;top:0;width:1200px;height:723px;overflow:hidden}
.hero-media{position:absolute;inset:0;background:
  radial-gradient(ellipse 420px 380px at 1000px 330px,#c8324e 0%,#9b2140 45%,transparent 75%),
  radial-gradient(ellipse 380px 300px at 160px 420px,#e9dcb7 0%,#7c8aa8 50%,transparent 80%),
  linear-gradient(90deg,#4f6fa3 0%,#3b3f7a 45%,#6a2a5e 70%,#8f1f3c 100%)}
.hero-shade{position:absolute;inset:0;background:linear-gradient(180deg,rgba(20,20,60,.35),rgba(30,30,80,.15))}
.logo{font-family:"Syncopate",sans-serif;font-weight:400;color:var(--white);font-size:25px;line-height:27px;letter-spacing:1px;text-transform:uppercase}
.nav{display:flex;gap:0;font-size:12px;font-weight:700;color:var(--white);letter-spacing:.5px}
.nav span{position:absolute;white-space:nowrap}
.btn{left:997px;top:25px;width:151px;height:41px;border-radius:21px;background:linear-gradient(90deg,var(--purple),var(--blue-mid));color:var(--white);font-size:12px;font-weight:700;display:flex;align-items:center;justify-content:center;letter-spacing:.5px}
.badge{left:400px;top:229px;width:400px;height:30px;background:var(--purple);color:var(--white);font-size:14px;font-weight:500;display:flex;align-items:center;justify-content:center;letter-spacing:.5px}
.hero h1{top:280px;font-size:32px;line-height:38px;color:var(--white)}
.hero p{top:362px;color:var(--white);font-size:15px;line-height:21px}

/* intro */
.intro-title{top:735px;font-size:27px;line-height:34px}
.intro-copy{left:145px;width:910px;top:828px;font-size:15px;line-height:20px;text-align:center}
.intro-copy p+p{margin-top:20px}
.care-lead{left:140px;top:1022px;width:480px;font-size:14.5px;line-height:19px}
.care-item{left:138px;width:500px;height:80px}
.care-icon{position:absolute;left:0;top:0;width:76px;height:76px;border-radius:50%;border:4px solid var(--blue);border-right-color:transparent;display:flex;align-items:center;justify-content:center}
.care-icon.purple{border-color:var(--purple);border-right-color:transparent}
.care-icon.teal{border-color:var(--teal-light);border-right-color:transparent}
.care-item p{position:absolute;left:92px;top:14px;width:350px;font-size:14px;line-height:18px;color:var(--ink)}
.robot{left:640px;top:985px;width:520px;height:440px}

/* about */
.about{left:78px;top:1522px;width:1050px;height:496px;border-radius:10px;overflow:hidden;background:linear-gradient(110deg,var(--blue) 30%,#4a4fa8 65%,var(--purple) 100%)}
.about-photo{position:absolute;left:0;top:0;width:540px;height:496px;clip-path:polygon(0 0,80% 0,100% 50%,80% 100%,0 100%);background:linear-gradient(135deg,#d9d7d2,#b8b2a6 55%,#7d7268)}
.about-text{position:absolute;left:568px;top:92px;width:450px;color:var(--white)}
.about-text .display{color:var(--white);font-size:24px;line-height:32px}
.about-text p{font-size:14px;line-height:19px;margin-top:22px}
.about-text p+p{margin-top:20px}

/* approach */
.approach-title{top:2125px;font-size:26px}
.approach-lead{top:2192px;font-size:17px;line-height:27px}
.approach-ring{left:60px;top:2292px;width:500px;height:500px}
.approach-card{left:690px;width:425px;height:116px;background:var(--white);border-radius:60px 20px 20px 60px;box-shadow:0 8px 26px rgba(40,40,90,.12)}
.num{position:absolute;left:14px;top:16px;width:84px;height:84px;border-radius:50%;color:var(--white);font-family:"Syncopate",sans-serif;font-size:30px;display:flex;align-items:center;justify-content:center}
.num.teal{background:var(--teal-light)}
.num.purple{background:var(--purple)}
.approach-card p{position:absolute;left:122px;top:32px;width:275px;font-size:14px;line-height:22px;font-weight:600;color:var(--ink)}
.approach-foot{top:2834px;font-size:17px;line-height:27px}

/* 3d */
.tech{left:0;top:2943px;width:1200px;height:516px;background:var(--pale);overflow:hidden}
.tech-media{position:absolute;left:590px;top:0;width:610px;height:516px;clip-path:polygon(22% 0,100% 0,100% 100%,0 100%);background:radial-gradient(ellipse 260px 220px at 380px 240px,#d8424d 0%,#8b2c55 45%,transparent 75%),linear-gradient(135deg,#3e7fc8,#1b4e9a)}
.tech-edge{position:absolute;left:590px;top:0;width:140px;height:516px;clip-path:polygon(95% 0,100% 0,5% 100%,0 100%);background:var(--blue-mid)}
.side-line{height:2px;background:var(--blue-mid)}
.tech .display{position:absolute;left:130px;top:95px;font-size:24px;line-height:34px}
.tech p{position:absolute;left:130px;top:193px;width:480px;font-size:16px;line-height:24px}

/* pre-procedure */
.pre{left:0;top:3459px;width:1200px;height:543px;background:linear-gradient(100deg,var(--blue-mid) 30%,var(--cyan) 60%,var(--teal-light) 100%);overflow:hidden}
.pre-media{position:absolute;left:0;top:0;width:640px;height:543px;clip-path:polygon(0 0,100% 0,82% 100%,0 100%);background:radial-gradient(ellipse 200px 200px at 260px 300px,#9ed2f0 0%,transparent 70%),linear-gradient(135deg,#2b7fd0,#1a5fb0 60%,#174e95)}
.pre-text{position:absolute;left:688px;top:70px;width:460px;color:var(--white)}
.pre-text .display{color:var(--white);font-size:24px;line-height:32px}
.pre-text > p{font-size:16px;line-height:26px;margin-top:24px}
.pre-point{position:relative;padding-left:46px;margin-top:24px;font-size:14.5px;line-height:26px;font-weight:600}
.pre-point svg{position:absolute;left:0;top:2px}

/* post-op */
.post-title{top:4066px;font-size:26px}
.post-lead{top:4130px;font-size:17px;line-height:27px}
.hex{width:273px;height:300px;filter:drop-shadow(0 8px 18px rgba(40,40,90,.14))}
.hex-inner{width:100%;height:100%;background:var(--white);clip-path:polygon(50% 0,100% 22%,100% 78%,50% 100%,0 78%,0 22%)}
.hex-icon{position:absolute;left:96px;top:56px;width:80px;height:80px;border-radius:50%;display:flex;align-items:center;justify-content:center}
.hex p{position:absolute;left:40px;width:193px;top:160px;text-align:center;font-size:14px;line-height:22px;font-weight:600;color:var(--ink)}
.post-foot{top:4552px;font-size:17px;line-height:27px}

/* commitment */
.navy-band{left:0;top:5014px;width:1200px;height:310px;background:var(--navy)}
.commit{left:103px;top:4657px;width:994px;height:427px;border-radius:8px;background:linear-gradient(110deg,var(--blue-mid),#2f63b6 50%,var(--purple));color:var(--white);text-align:center}
.commit .display{position:absolute;top:98px;left:0;width:100%;color:var(--white);font-size:28px;line-height:36px}
.commit p{position:absolute;top:194px;left:110px;width:774px;font-size:17px;line-height:27px;color:#e4e6f8}

/* footer */
.footer-logo{left:136px;top:5152px;font-size:24px;line-height:26px}
.footer-nav{top:5172px;font-size:12.5px;font-weight:700;color:var(--white)}
.footer-nav span{position:absolute;white-space:nowrap}
.footer-rule{left:0;top:5235px;width:1200px;height:1px;background:rgba(255,255,255,.15)}
.copy{top:5264px;font-size:12px;color:#cfd0e6}
.social{top:5263px;width:20px;height:20px;border-radius:50%;background:var(--white)}
</style>
</head>
<body>

<!-- HERO -->
<section class="abs hero">
  <div class="hero-media" role="img" aria-label="Robotic surgical arms operating beside a large red kidney illustration"></div>
  <div class="hero-shade"></div>
  <div class="abs logo" style="left:93px;top:26px">Dr Renato<br>Vilhena</div>
  <nav class="nav">
    <span style="left:330px;top:39px">HOME</span>
    <span style="left:415px;top:39px">ABOUT</span>
    <span style="left:508px;top:39px">APPROACH</span>
    <span style="left:630px;top:39px">3D TECHNOLOGY</span>
    <span style="left:795px;top:39px">SUPPORT</span>
    <span style="left:905px;top:39px">CARE</span>
  </nav>
  <div class="abs btn">COMMITMENT</div>
  <div class="abs badge">WELCOME TO DR. RENATO VILHENA</div>
  <h1 class="abs display center"><span class="light">Caring with precision,</span><span class="bold">Treating with empathy</span></h1>
  <p class="abs center">Robotic surgery represents one of the most relevant advances in modern medicine.<br>It offers more accuracy, less bleeding and faster recovery</p>
  <svg class="abs" style="left:0;top:620px" width="1200" height="104" viewBox="0 0 1200 104">
    <defs><linearGradient id="curveLine" x1="0" x2="1"><stop offset="0" stop-color="#0054AA"/><stop offset=".5" stop-color="#6B429C"/><stop offset="1" stop-color="#0677BA"/></linearGradient></defs>
    <path d="M0 104 L0 100 Q600 -10 1200 60 L1200 104 Z" fill="#fff"/>
    <path d="M230 72 Q600 22 1130 50" fill="none" stroke="url(#curveLine)" stroke-width="5"/>
    <line x1="600" y1="40" x2="600" y2="72" stroke="#6B429C" stroke-width="1.5"/>
    <circle cx="600" cy="76" r="3.5" fill="#6B429C"/>
  </svg>
</section>

<!-- INTRO -->
<h2 class="abs display center intro-title" style="font-size:27px"><span class="light">Caring with precision,</span><span class="bold">Treating with empathy</span></h2>
<div class="abs intro-copy">
  <p>Robotic surgery represents one of the most relevant advances in modern medicine. It offers more accuracy, less bleeding and faster recovery. But, above technology, there is the commitment to the best decision for each patient.</p>
  <p>Here, we understand that not every case needs surgery, and much less that every surgery needs to be robotic. We work based on the best scientific evidence, international guidelines and, when necessary, with the support of artificial intelligence technologies to help define the most appropriate conduct.</p>
</div>

<p class="abs care-lead">But our care goes beyond the operating room. We know that a good outcome also depends on how the patient gets to the hospital and how he returns home. That's why we offer:</p>

<div class="abs care-item" style="top:1117px">
  <div class="care-icon"><svg width="34" height="34" viewBox="0 0 34 34" fill="none" stroke="#0054AA" stroke-width="2"><rect x="6" y="4" width="20" height="26" rx="2"/><line x1="11" y1="11" x2="21" y2="11"/><line x1="11" y1="16" x2="21" y2="16"/><line x1="11" y1="21" x2="17" y2="21"/></svg></div>
  <p>An administrative team that takes care of all contact with hospitals and health plans, avoiding wear and tear with bureaucracies.</p>
</div>
<div class="abs care-item" style="top:1226px">
  <div class="care-icon purple"><svg width="34" height="34" viewBox="0 0 34 34" fill="none" stroke="#6B429C" stroke-width="2"><rect x="4" y="7" width="26" height="18" rx="2"/><polyline points="8,17 12,17 14,12 17,21 19,15 26,15"/><line x1="13" y1="29" x2="21" y2="29"/></svg></div>
  <p>A group of nurses and physiotherapists who monitor the postoperative period with visits and guidance at home.</p>
</div>
<div class="abs care-item" style="top:1333px">
  <div class="care-icon teal"><svg width="34" height="34" viewBox="0 0 34 34" fill="none" stroke="#00BBA5" stroke-width="2"><rect x="4" y="6" width="18" height="13" rx="2"/><rect x="12" y="15" width="18" height="13" rx="2"/></svg></div>
  <p>A direct contact channel to clarify doubts and ensure peace of mind throughout the process.</p>
</div>

<svg class="abs robot" viewBox="0 0 520 440" role="img" aria-label="Surgical robot system beside an illustrated kidney inside a circular frame">
  <defs><linearGradient id="ring1" x1="0" y1="1" x2="1" y2="0"><stop offset="0" stop-color="#6B429C"/><stop offset="1" stop-color="#0677BA"/></linearGradient>
  <radialGradient id="robotFill" cx=".5" cy=".5" r=".6"><stop offset="0" stop-color="#e7e3f2"/><stop offset=".7" stop-color="#cfc8e6"/><stop offset="1" stop-color="#b7a5ce"/></radialGradient></defs>
  <circle cx="262" cy="220" r="214" fill="none" stroke="url(#ring1)" stroke-width="10" stroke-dasharray="900 450" transform="rotate(100 262 220)"/>
  <circle cx="262" cy="220" r="200" fill="url(#robotFill)"/>
</svg>

<!-- ABOUT -->
<section class="abs about">
  <div class="about-photo" role="img" aria-label="Portrait of the doctor in a white coat smiling at his desk"></div>
  <div class="about-text">
    <h2 class="display"><span class="light">About</span><span class="bold">Dr. Renato Vilhena</span></h2>
    <p>Caring with precision, treating with empathy! I am a urologist with a focus on robotic surgery and comprehensive patient care. More than a technique, I believe that good medicine begins with listening, careful planning, and commitment to what is best for each person.</p>
    <p>My mission is to offer treatments based on science, technology, and humanity — respecting each patient's time, choices, and goals.</p>
  </div>
</section>

<!-- APPROACH -->
<h2 class="abs display center approach-title"><span class="light" style="display:inline">Our </span><span class="bold" style="display:inline">Approach</span><div class="rule"></div></h2>
<p class="abs center approach-lead">Not every treatment needs to be surgical. Not every surgery needs to be robotic.<br>Robotic surgery is a great advance, but it must be indicated with criteria. Before proposing any<br>intervention, we evaluate the case broadly:</p>

<svg class="abs approach-ring" viewBox="0 0 500 500" role="img" aria-label="Close-up photograph of a robotic procedure with surgical instruments">
  <defs><radialGradient id="tissue" cx=".45" cy=".45" r=".6"><stop offset="0" stop-color="#c98a70"/><stop offset=".6" stop-color="#8a3d32"/><stop offset="1" stop-color="#4a1f22"/></radialGradient></defs>
  <circle cx="245" cy="253" r="236" fill="none" stroke="#6B429C" stroke-width="2"/>
  <path d="M245 17 A236 236 0 0 0 70 412" fill="none" stroke="#00BBA5" stroke-width="18" transform="translate(0 0)"/>
  <circle cx="245" cy="253" r="222" fill="url(#tissue)"/>
  <circle cx="116" cy="30" r="6" fill="#0054AA"/>
  <circle cx="364" cy="486" r="6" fill="#6B429C"/>
</svg>
<svg class="abs" style="left:528px;top:2330px" width="170" height="430" viewBox="0 0 170 430" fill="none">
  <path d="M0 215 L70 215 Q100 215 110 180 L150 35 Q155 20 170 18" stroke="#8fc8ea" stroke-width="3"/>
  <path d="M0 215 L170 215" stroke="#8fc8ea" stroke-width="3"/>
  <path d="M0 215 L70 215 Q100 215 110 250 L150 395 Q155 410 170 412" stroke="#8fc8ea" stroke-width="3"/>
  <line x1="0" y1="215" x2="90" y2="215" stroke="#b9dcf2" stroke-width="10" stroke-dasharray="2 4"/>
</svg>

<div class="abs approach-card" style="top:2333px"><div class="num teal">01</div><p>We use the most up-to-date medical guidelines.</p></div>
<div class="abs approach-card" style="top:2478px"><div class="num purple">02</div><p style="top:22px">We make use of artificial intelligence tools to support clinical decision-making</p></div>
<div class="abs approach-card" style="top:2650px"><div class="num teal">03</div><p style="top:22px">We conduct frank conversations about the real needs, benefits and risks of each approach.</p></div>

<p class="abs center approach-foot">Our focus is to ensure that the patient is referred to the option with the greatest potential<br>for outcome — be it surgical, clinical, or even active surveillance.</p>

<!-- 3D TECHNOLOGY -->
<section class="abs tech">
  <div class="tech-media" role="img" aria-label="3D rendering of two kidneys with blood vessels"></div>
  <div class="tech-edge"></div>
  <div class="abs side-line" style="left:0;top:104px;width:92px"></div>
  <div class="abs" style="left:88px;top:99px;width:12px;height:12px;border-radius:50%;background:var(--blue-mid)"></div>
  <h2 class="display"><span class="light">Planning with</span><span class="bold">3D Technology</span></h2>
  <p>In kidney and prostate surgeries, we adopt the use of personalized 3D models, created from the patient's own exams. These models help to understand the anatomy precisely, making it easier to choose the best surgical approach. We have already demonstrated that this planning reduces bleeding, surgical time, and even changes the strategy in almost half of the cases evaluated.</p>
</section>

<!-- PRE-PROCEDURE -->
<section class="abs pre">
  <div class="pre-media" role="img" aria-label="Nurse in blue scrubs holding a tablet with a holographic kidney diagram"></div>
  <div class="abs side-line" style="left:1112px;top:97px;width:88px;background:#fff"></div>
  <div class="abs" style="left:1106px;top:92px;width:12px;height:12px;border-radius:50%;background:#fff"></div>
  <div class="pre-text">
    <h2 class="display"><span class="light">Pre-procedure</span><span class="bold">Support</span></h2>
    <p>Your focus should be on your health, not bureaucracy. We know that the moment before a procedure can be surrounded by doubts and anxiety. That's why we offer:</p>
    <div class="pre-point"><svg width="30" height="30" viewBox="0 0 30 30"><circle cx="15" cy="15" r="14" fill="#fff"/><polyline points="12,9 18,15 12,21" fill="none" stroke="#00A9DD" stroke-width="2.5"/></svg>An office dedicated to solving all the bureaucratic part with hospitals and health plans;</div>
    <div class="pre-point"><svg width="30" height="30" viewBox="0 0 30 30"><circle cx="15" cy="15" r="14" fill="#fff"/><polyline points="12,9 18,15 12,21" fill="none" stroke="#00A9DD" stroke-width="2.5"/></svg>Close, agile and human support, so that you can focus on what really matters: your preparation and well-being.</div>
  </div>
</section>

<!-- POSTOPERATIVE -->
<h2 class="abs display center post-title"><span class="light" style="display:inline">Postoperative </span><span class="bold" style="display:inline">Care</span><div class="rule"></div></h2>
<p class="abs center post-lead"><strong style="color:var(--ink)">Recovering well is an essential part of the treatment.</strong><br>After being discharged from the hospital, we continued by his side. Our team of<br>nurses and physiotherapists offers:</p>

<div class="abs hex" style="left:161px;top:4223px"><div class="hex-inner"></div>
  <div class="hex-icon" style="background:linear-gradient(135deg,#0677BA,#6B429C)"><svg width="40" height="40" viewBox="0 0 40 40" fill="none" stroke="#fff" stroke-width="2"><path d="M6 20 L20 8 L34 20"/><rect x="11" y="19" width="18" height="14"/><rect x="17" y="24" width="6" height="9"/></svg></div>
  <p style="top:175px">Home visits when necessary;</p></div>
<div class="abs hex" style="left:469px;top:4223px"><div class="hex-inner"></div>
  <div class="hex-icon" style="background:linear-gradient(135deg,#00A9DD,#00BBA5)"><svg width="40" height="40" viewBox="0 0 40 40" fill="none" stroke="#fff" stroke-width="2"><rect x="10" y="7" width="20" height="27" rx="2"/><line x1="15" y1="14" x2="25" y2="14"/><line x1="15" y1="20" x2="25" y2="20"/><line x1="15" y1="26" x2="21" y2="26"/></svg></div>
  <p>Practical guidance on movement, feeding and medications</p></div>
<div class="abs hex" style="left:774px;top:4223px"><div class="hex-inner"></div>
  <div class="hex-icon" style="background:linear-gradient(135deg,#6B429C,#A7469A)"><svg width="40" height="40" viewBox="0 0 40 40" fill="none" stroke="#fff" stroke-width="2"><rect x="9" y="8" width="18" height="24" rx="2"/><circle cx="26" cy="24" r="5"/><line x1="30" y1="28" x2="34" y2="32"/><line x1="13" y1="14" x2="23" y2="14"/></svg></div>
  <p style="top:150px">Monitoring of signs that deserve attention — always with an attentive clinical eye.</p></div>

<p class="abs center post-foot">In addition, we maintain a direct contact channel to clarify doubts, adapt<br>conducts and support your recovery.</p>

<!-- COMMITMENT -->
<div class="abs navy-band"></div>
<section class="abs commit">
  <h2 class="display"><span class="light">Commitment to</span><span class="bold">the patient</span></h2>
  <p>We believe that the best result comes from the sum of knowledge, technology and empathy. Our commitment is to deeply understand what you are facing, clearly present all available options and build, together, the best path for your treatment. Because each patient is unique — and deserves to be cared for as such.</p>
</section>

<!-- FOOTER -->
<div class="abs logo footer-logo">Dr Renato<br>Vilhena</div>
<nav class="abs footer-nav" style="left:0;width:1200px">
  <span style="left:385px">HOME</span>
  <span style="left:462px">ABOUT</span>
  <span style="left:547px">APPROACH</span>
  <span style="left:662px">3D TECHNOLOGY</span>
  <span style="left:818px">SUPPORT</span>
  <span style="left:918px">CARE</span>
  <span style="left:994px">COMMITMENT</span>
</nav>
<div class="abs footer-rule"></div>
<p class="abs center copy">Copyright © 2025 Dr. Renato Vilhena. All Right Reserved</p>
<div class="abs social" style="left:938px"></div>
<div class="abs social" style="left:981px"></div>
<div class="abs social" style="left:1023px"></div>
<div class="abs social" style="left:1064px"></div>

</body>
</html>
```